Quote Cards for Social Media RV

I would like to put these quotes over one of the pictures attached; One Quote per picture, and I want the quote to be bold or easy to read as well. I provided a few reference graphics that I really like as examples below. In very small letters at the bottom add @RVCarloweDaily

All of the pictures are attached; you can pick any photo and add one quote to it; but no stock photography

Target Market(s)

women trying to lose weight

Requirements
Must have
• quotes and pictures attached
Should not have
• no stock photography

```html
<!DOCTYPE html>
<html lang="en">
<head>
<meta charset="UTF-8">
<title>Quote Card – RV</title>
<link href="https://fonts.googleapis.com/css2?family=Poppins:ital,wght@0,500;0,700;1,700&display=swap" rel="stylesheet">
<style>
  :root {
    --stage-deep: #2a2370;
    --stage-violet: #5a46b8;
    --stage-orange: #ff6a3a;
    --stage-pink: #e0249a;
    --gown-magenta: #d81e8e;
    --panel-tint: rgba(38, 30, 72, 0.62);
    --frame-white: #ffffff;
    --text-white: #ffffff;
  }
  html, body {
    margin: 0;
    padding: 0;
    width: 1200px;
    height: 1200px;
    overflow: hidden;
    background: var(--stage-deep);
  }
  .quote-card {
    position: relative;
    width: 1200px;
    height: 1200px;
    overflow: hidden;
    font-family: "Poppins", sans-serif;
  }
  .card-photo {
    position: absolute;
    inset: 0;
    background:
      radial-gradient(ellipse 160px 520px at 740px 720px, var(--gown-magenta) 0%, rgba(216,30,142,0.6) 55%, rgba(216,30,142,0) 100%),
      radial-gradient(ellipse 340px 300px at 360px 60px, rgba(255,150,60,0.85) 0%, rgba(255,150,60,0) 100%),
      radial-gradient(ellipse 260px 700px at 1010px 380px, rgba(255,110,70,0.75) 0%, rgba(255,110,70,0) 100%),
      linear-gradient(100deg, var(--stage-orange) 0%, var(--stage-pink) 18%, var(--stage-violet) 45%, #6a5ad0 70%, var(--stage-deep) 100%);
  }
  .card-photo::after {
    content: "";
    position: absolute;
    left: 0; right: 0; bottom: 0;
    height: 300px;
    background: linear-gradient(180deg, rgba(20,16,50,0) 0%, rgba(20,16,50,0.85) 100%);
  }
  .quote-panel {
    position: absolute;
    left: 91px;
    top: 294px;
    width: 492px;
    height: 676px;
    border-radius: 34px;
    background: var(--panel-tint);
  }
  .quote-frame {
    position: absolute;
    inset: 0;
  }
  .quote-text {
    position: absolute;
    left: 91px;
    top: 352px;
    width: 492px;
    margin: 0;
    text-align: center;
    color: var(--text-white);
    font-weight: 700;
    font-style: italic;
    font-size: 49px;
    line-height: 65px;
    letter-spacing: 0.2px;
  }
  .quote-handle {
    position: absolute;
    left: 0;
    width: 1200px;
    top: 1120px;
    text-align: center;
    padding-left: 0;
    color: var(--text-white);
    font-weight: 500;
    font-size: 22px;
    transform: translateX(0);
  }
  .quote-handle span {
    position: absolute;
    left: 490px;
  }
</style>
</head>
<body>
  <main class="quote-card">
    <div class="card-photo" role="img" aria-label="Photo of a smiling woman in a long-sleeved magenta gown posing on a stage lit with purple and orange light bars"></div>

    <div class="quote-panel"></div>

    <svg class="quote-frame" width="1200" height="1200" viewBox="0 0 1200 1200" aria-hidden="true">
      <path d="M130 237 H94 A50 50 0 0 0 44 287 V973 A50 50 0 0 0 94 1023 H367
               M533 1023 H580 A50 50 0 0 0 630 973 V287 A50 50 0 0 0 580 237 H262"
            fill="none" stroke="var(--frame-white)" stroke-width="6" stroke-linecap="round"/>
      <text x="146" y="330" fill="var(--frame-white)" font-family="Poppins, sans-serif" font-weight="700" font-size="190">“</text>
      <text x="424" y="1114" fill="var(--frame-white)" font-family="Poppins, sans-serif" font-weight="700" font-size="190">”</text>
    </svg>

    <p class="quote-text">Struggling<br>with bloating<br>and belly fat?<br>Try this<br>natural<br>solution<br>tonight, and<br>wake up<br>feeling lighter!</p>

    <div class="quote-handle"><span>@RVCarloweDaily</span></div>
  </main>
</body>
</html>
```